Logo for Internal Medicine practice

I want a logo for my Internal Medicine practice, I would like it to be with my name on it which is Lucía Barrenechea Ruiz.

I would like the business card to say the following (it is in Spanish since my practice is in Spanish):

Lucía Barrenechea Ruiz
Medicina Interna
Cel. 5583617204
luciabarrenechearuiz@correovela.mx

Logo Text

Lucía Barrenechea

```html
<!DOCTYPE html>
<html lang="es">
<head>
<meta charset="utf-8">
<title>Lucía Barrenechea Ruiz — Tarjeta de presentación</title>
<link rel="stylesheet" href="https://fonts.googleapis.com/css2?family=Michroma&family=Poppins:wght@400;700&display=swap">
<style>
  :root {
    --brand-blue: #0596ff;
    --paper: #ffffff;
    --backdrop: #e3e3e1;
  }
  * { margin: 0; padding: 0; box-sizing: border-box; }
  html, body {
    width: 1200px;
    height: 802px;
    overflow: hidden;
    background: var(--backdrop);
  }
  .sheet {
    position: relative;
    width: 1200px;
    height: 802px;
  }
  .card {
    position: absolute;
    top: 246px;
    width: 540px;
    height: 310px;
    border-radius: 26px;
    background: var(--brand-blue);
    overflow: hidden;
    color: var(--paper);
  }
  .card--contact { left: 50px; }
  .card--brand { left: 610px; }

  .contact-art {
    position: absolute;
    inset: 0;
  }
  .contact-info {
    position: absolute;
    right: 32px;
    top: 92px;
    width: 330px;
    text-align: right;
    font-family: "Poppins", sans-serif;
    white-space: nowrap;
  }
  .contact-name {
    font-weight: 700;
    font-size: 19px;
    letter-spacing: 0.02em;
    text-transform: uppercase;
    line-height: 24px;
  }
  .contact-role {
    font-weight: 400;
    font-size: 15px;
    line-height: 22px;
    letter-spacing: 0.03em;
  }
  .contact-divider {
    height: 2px;
    background: var(--paper);
    margin: 10px 0 12px;
  }
  .contact-list {
    list-style: none;
  }
  .contact-item {
    display: flex;
    justify-content: flex-end;
    align-items: center;
    gap: 10px;
    font-size: 15px;
    line-height: 22px;
    letter-spacing: 0.03em;
  }
  .contact-item--email { font-size: 12px; letter-spacing: 0.01em; }
  .contact-icon { width: 11px; height: 11px; flex: none; }

  .brand-lockup {
    position: absolute;
    left: 42px;
    top: 104px;
    display: flex;
    align-items: center;
    gap: 22px;
  }
  .brand-dot {
    width: 96px;
    height: 96px;
    border-radius: 50%;
    background: var(--paper);
    flex: none;
  }
  .brand-name {
    font-family: "Michroma", sans-serif;
    font-weight: 400;
    font-size: 25px;
    line-height: 1.25;
    text-transform: uppercase;
    color: var(--paper);
  }
</style>
</head>
<body>
<main class="sheet">
  <section class="card card--contact" aria-label="Tarjeta, anverso">
    <svg class="contact-art" width="540" height="310" viewBox="0 0 540 310" aria-hidden="true">
      <circle cx="115" cy="305" r="150" fill="#ffffff"/>
    </svg>
    <div class="contact-info">
      <h1 class="contact-name">Lucía Barrenechea Ruiz</h1>
      <p class="contact-role">Medicina Interna</p>
      <div class="contact-divider" aria-hidden="true"></div>
      <ul class="contact-list">
        <li class="contact-item">
          <span>5583617204</span>
          <svg class="contact-icon" viewBox="0 0 12 12" aria-hidden="true">
            <rect x="3" y="0.8" width="6" height="10.4" rx="1.2" fill="none" stroke="#ffffff" stroke-width="1.4"/>
          </svg>
        </li>
        <li class="contact-item contact-item--email">
          <span>luciabarrenechearuiz@correovela.mx</span>
          <svg class="contact-icon" viewBox="0 0 12 12" aria-hidden="true">
            <rect x="0.5" y="2" width="11" height="8" fill="#ffffff"/>
            <path d="M0.5 2 L6 6.5 L11.5 2" fill="none" stroke="#0596ff" stroke-width="1.2"/>
          </svg>
        </li>
      </ul>
    </div>
  </section>

  <section class="card card--brand" aria-label="Tarjeta, reverso">
    <div class="brand-lockup">
      <span class="brand-dot" aria-hidden="true"></span>
      <p class="brand-name">Lucía<br>Barrenechea</p>
    </div>
  </section>
</main>
</body>
</html>
```